Design a New Business Card for Our Company

We are looking for fresh, unique, and a modern business card that reflects our roots as digital marketing agency focused on SEM.

Industry/Entity Type

Marketing

Contact Information for Business Card

looking for very unique out of the box designs. clean and modern that compliments our logo

Requirements
Must have
• colors should match our logo
• Front should have name, address, email, and phone/fax of the person, phone/fax are the same number
• back should have our url

```html
<!DOCTYPE html>
<html lang="en">
<head>
<meta charset="utf-8">
<title>Brightway Media – Business Card</title>
<link href="https://fonts.googleapis.com/css2?family=Open+Sans:wght@400;600;700&display=swap" rel="stylesheet">
<style>
  :root {
    --canvas: #e6e7ea;
    --navy: #15304f;
    --charcoal: #323334;
    --sky: #5b9be0;
    --silver: #c9cacc;
    --white: #f4f5f6;
    --strip: #b9bbbe;
    --url: #1f3b63;
  }
  * { box-sizing: border-box; margin: 0; padding: 0; }
  html, body { width: 1200px; height: 716px; overflow: hidden; }
  body {
    background: var(--canvas);
    font-family: "Open Sans", Arial, sans-serif;
    position: relative;
  }
  .card {
    position: absolute;
    width: 520px;
    height: 297px;
    border-radius: 3px;
    box-shadow: 0 10px 28px rgba(0,0,0,.22);
    overflow: hidden;
  }
  .card--back { left: 50px; top: 70px; background: var(--navy); }
  .card--front { left: 630px; top: 349px; background: var(--charcoal); }

  .brand {
    position: absolute;
    display: flex;
    align-items: center;
    gap: 12px;
    color: var(--sky);
    font-weight: 700;
    letter-spacing: .5px;
    white-space: nowrap;
  }
  .brand__dot { border-radius: 50%; background: var(--sky); flex: none; }
  .card--back .brand { left: 50%; top: 50%; transform: translate(-50%, -50%); font-size: 44px; }
  .card--back .brand__dot { width: 30px; height: 30px; }
  .card--front .brand { left: 40px; top: 34px; font-size: 28px; }
  .card--front .brand__dot { width: 20px; height: 20px; }

  .person { position: absolute; left: 40px; top: 96px; }
  .person__name { color: var(--sky); font-weight: 600; font-size: 17px; line-height: 1.1; }
  .person__role { color: var(--white); font-weight: 600; font-size: 13px; margin-bottom: 8px; }
  .contact { list-style: none; }
  .contact li {
    display: flex; align-items: center; gap: 7px;
    color: var(--white); font-size: 13px; line-height: 20px;
    white-space: nowrap;
  }
  .contact svg { width: 12px; height: 12px; flex: none; fill: none; stroke: var(--white); stroke-width: 1.6; }

  .strip {
    position: absolute; left: 0; right: 0; bottom: 0; height: 20px;
    background: var(--strip);
  }
  .url-tab {
    position: absolute; right: 0; bottom: 0; height: 34px;
    background: var(--strip);
    clip-path: polygon(18px 0, 100% 0, 100% 100%, 0 100%);
    display: flex; align-items: center; gap: 7px;
    padding: 0 18px 0 30px;
    color: var(--url); font-weight: 700; font-size: 13px;
    white-space: nowrap;
  }
  .url-tab svg { width: 14px; height: 14px; flex: none; fill: none; stroke: var(--url); stroke-width: 1.6; }
</style>
</head>
<body>
  <section class="card card--back" aria-label="Card back">
    <div class="brand"><span class="brand__dot"></span>Brightway Media</div>
  </section>

  <section class="card card--front" aria-label="Card front">
    <div class="brand"><span class="brand__dot"></span>Brightway Media</div>

    <div class="person">
      <p class="person__name">Marlowe</p>
      <p class="person__role">Chairman</p>
      <ul class="contact">
        <li><svg viewBox="0 0 12 12"><path d="M3 1l2 2.5-1.2 1.3a6 6 0 0 0 3.4 3.4L8.5 7 11 9l-1.3 2A9 9 0 0 1 1 2.3z"/></svg>0198765432</li>
        <li><svg viewBox="0 0 12 12"><rect x="1" y="5" width="10" height="6"/><path d="M3 5V1h6v4M3 8h6"/></svg>0198765432</li>
        <li><svg viewBox="0 0 12 12"><rect x="1" y="2.5" width="10" height="7"/><path d="M1 2.5l5 4 5-4"/></svg>hello@brightway.com</li>
        <li><svg viewBox="0 0 12 12"><path d="M6 11S2 7 2 4.5a4 4 0 0 1 8 0C10 7 6 11 6 11z"/><circle cx="6" cy="4.5" r="1.3"/></svg>12 harbor lane, austin, tx 78701</li>
      </ul>
    </div>

    <div class="strip"></div>
    <div class="url-tab">
      <svg viewBox="0 0 14 14"><circle cx="7" cy="7" r="6"/><path d="M1 7h12M7 1c-3 3-3 9 0 12M7 1c3 3 3 9 0 12"/></svg>
      <span class="url-tab__text">www.brightwaymedia.com</span>
    </div>
  </section>
</body>
</html>
```